Business Card Design using new attached logo

We are a family run Plumbing and Heating firm looking to improve our company image with an improved business card and new logo.We are looking to keep the company colour (Blue) involved in our design

Reason: New logo added which needs to be incorporated on designs

Industry/Entity Type

Business

Contact Information for Business Card

See attachment of all info required.

Requirements
Must have
• We have just picked a new company logo which is attached.
• Could you please provide your business card designs using this logo.
• We are looking for the logo on the back as well as the front with all the info required

```html
<!DOCTYPE html>
<html lang="en">
<head>
<meta charset="utf-8">
<title>Kestrel Heating Ltd – Business Card</title>
<link rel="stylesheet" href="https://fonts.googleapis.com/css2?family=Open+Sans:wght@400;600&display=swap">
<style>
  :root {
    --navy: #1f386c;
    --blue-light: #3a7fc2;
    --band-grey: #858585;
    --divider: #9a9a9a;
    --ink: #1a1a1a;
    --paper: #ffffff;
  }
  html, body {
    margin: 0;
    padding: 0;
    width: 1200px;
    height: 790px;
    overflow: hidden;
    background: var(--paper);
  }
  .card {
    position: relative;
    width: 1200px;
    height: 790px;
    background: var(--paper);
    font-family: "Open Sans", Arial, sans-serif;
    overflow: hidden;
  }
  .card__sweep {
    position: absolute;
    inset: 0;
    width: 1200px;
    height: 790px;
  }
  .brand-name {
    position: absolute;
    left: 100px;
    top: 478px;
    width: 470px;
    margin: 0;
    font-weight: 600;
    font-size: 62px;
    line-height: 1.05;
    letter-spacing: 4px;
    color: var(--navy);
    text-transform: uppercase;
  }
  .divider {
    position: absolute;
    left: 596px;
    top: 398px;
    width: 2px;
    height: 278px;
    background: linear-gradient(to bottom, rgba(154,154,154,0), var(--divider) 20%, var(--divider) 80%, rgba(154,154,154,0));
  }
  .address {
    position: absolute;
    left: 643px;
    top: 384px;
    margin: 0;
    font-style: normal;
    font-size: 28px;
    line-height: 38px;
    color: var(--ink);
  }
  .contact-icons {
    position: absolute;
    left: 641px;
    top: 512px;
    margin: 0;
    padding: 0;
    list-style: none;
  }
  .contact-icons li {
    height: 44px;
    display: flex;
    align-items: center;
  }
  .contact-icons svg {
    fill: var(--navy);
  }
</style>
</head>
<body>
<main class="card">
  <svg class="card__sweep" viewBox="0 0 1200 790" aria-hidden="true">
    <defs>
      <radialGradient id="sweep-blue" cx="600" cy="110" r="620" gradientUnits="userSpaceOnUse">
        <stop offset="0" stop-color="var(--blue-light)"/>
        <stop offset="1" stop-color="var(--navy)"/>
      </radialGradient>
    </defs>
    <path d="M0,410 C300,200 700,120 1200,175 L1200,182 C700,132 320,222 0,472 Z" fill="var(--band-grey)"/>
    <path d="M0,0 H1200 V175 C700,120 300,200 0,410 Z" fill="url(#sweep-blue)"/>
  </svg>

  <p class="brand-name">Kestrel<br>Heating</p>

  <div class="divider"></div>

  <address class="address">
    Kestrel Heating Ltd<br>
    14 Mill Lane, Harbour Road<br>
    Ashford, AB1 2CD
  </address>

  <ul class="contact-icons">
    <li aria-label="Telephone">
      <svg width="30" height="34" viewBox="0 0 30 34"><path d="M22 2 l6 5 -4 5 -4 -2 c-3 3 -6 8 -7 12 l4 1 -1 6 -7 3 C5 26 12 8 22 2 Z"/></svg>
    </li>
    <li aria-label="Fax">
      <svg width="30" height="30" viewBox="0 0 30 30"><rect x="8" y="2" width="14" height="9"/><rect x="3" y="12" width="24" height="10" rx="1"/><rect x="6" y="24" width="18" height="4"/></svg>
    </li>
    <li aria-label="Mobile">
      <svg width="26" height="38" viewBox="0 0 26 38"><rect x="16" y="0" width="3" height="8"/><rect x="3" y="7" width="20" height="30" rx="2"/><rect x="6" y="11" width="14" height="8" fill="#fff"/><g fill="#fff"><rect x="6" y="22" width="3" height="3"/><rect x="11.5" y="22" width="3" height="3"/><rect x="17" y="22" width="3" height="3"/><rect x="6" y="27" width="3" height="3"/><rect x="11.5" y="27" width="3" height="3"/><rect x="17" y="27" width="3" height="3"/></g></svg>
    </li>
    <li aria-label="Email">
      <svg width="34" height="24" viewBox="0 0 34 24"><rect x="1" y="2" width="32" height="20"/><path d="M1 2 L17 14 L33 2" fill="none" stroke="#fff" stroke-width="2"/></svg>
    </li>
  </ul>
</main>
</body>
</html>
```